Forward thinking startup needs business cards

We are a new company entering the fall protection market and we need business cards. We provide equipment and supplies to a very large industry, and we aim to catch the attention of the end-user; not just the distributors. Please browse brovatek.com for a better feel of our initial branding. The hog images are not required, but are here for inspiration. Also, they should not be prominent in the design as much as an accent. Many of our customers will be very high-end, so this should be considered as well.

Target Market(s)

Buyers for the safety industry. Some accounts will be very large, but most of these people are very down-to-earth.

Industry/Entity Type

Business

Contact Information for Business Card

Name and title
phone: 1-800-563-1804
fax: 740-555-0148
web: www.brovatek.com
address: 218 Kelbrook Lane, Dunmoor, OH 45790 USA
room for cell number, direct office phone number, extension, and email

Font styles to use
Serif
Sans Serif

Colors
f37122
ffffff

Requirements
Must have
• Should be very clean and easy to read. We typically use orange and grey in our color schemes - #ef7c2d and #424242
Nice to have
• It would be nice to have room somewhere to incorporate some of the other logos from our family of companies. At the same time, it should not look weird if they aren't included.

```html
<!DOCTYPE html>
<html lang="en">
<head>
<meta charset="utf-8">
<title>Brovatek Business Cards</title>
<link rel="stylesheet" href="https://fonts.googleapis.com/css2?family=Source+Sans+3:wght@400;600;800&display=swap">
<style>
  :root {
    --stage: #2a2a2a;
    --orange: #ef7c2d;
    --orange-light: #f39a4a;
    --grey: #424242;
    --white: #ffffff;
  }
  * { margin: 0; padding: 0; box-sizing: border-box; }
  html, body { width: 1200px; height: 750px; overflow: hidden; }
  body {
    background: var(--stage);
    font-family: "Source Sans 3", Arial, sans-serif;
    position: relative;
  }
  .card {
    position: absolute;
    top: 226px;
    width: 520px;
    height: 297px;
    overflow: hidden;
  }
  .card-back {
    left: 60px;
    background: linear-gradient(110deg, var(--orange) 0%, var(--orange) 55%, var(--orange-light) 72%, var(--orange) 90%);
  }
  .card-front { left: 620px; background: var(--white); }

  .brand-name {
    font-weight: 800;
    letter-spacing: 1px;
    line-height: 1;
    text-align: center;
  }
  .card-back .brand-name {
    position: absolute;
    top: 100px; left: 0; width: 100%;
    font-size: 50px;
    color: var(--white);
  }
  .back-web {
    position: absolute;
    top: 170px; left: 0; width: 100%;
    display: flex; justify-content: center; align-items: center; gap: 12px;
    color: var(--white);
    font-size: 13px;
    letter-spacing: 3px;
  }
  .back-web .rule { width: 70px; height: 1px; background: var(--white); opacity: .85; }
  .back-rule {
    position: absolute;
    top: 230px; left: 50%;
    width: 150px; height: 1px; margin-left: -75px;
    background: var(--white); opacity: .85;
  }

  .front-shape { position: absolute; inset: 0; }
  .card-front .brand-name {
    position: absolute;
    top: 64px; left: 80px; width: 300px;
    font-size: 48px;
    color: var(--orange);
  }
  .contact-list {
    position: absolute;
    top: 150px; right: 18px;
    list-style: none;
    color: var(--white);
    font-size: 12.5px;
    text-align: right;
  }
  .contact-list li {
    display: flex; justify-content: flex-end; align-items: center; gap: 6px;
    height: 19px;
  }
  .contact-list svg { width: 12px; height: 12px; flex: none; }
  .holder {
    position: absolute;
    left: 26px; top: 212px;
    color: var(--white);
    font-size: 12.5px;
    line-height: 15px;
  }
  .holder-name { font-size: 19px; font-weight: 600; line-height: 22px; }
</style>
</head>
<body>

<section class="card card-back" aria-label="Card back">
  <div class="brand-name">BROVATEK</div>
  <div class="back-web"><span class="rule"></span><span>www.brovatek.com</span><span class="rule"></span></div>
  <div class="back-rule"></div>
</section>

<section class="card card-front" aria-label="Card front">
  <svg class="front-shape" viewBox="0 0 520 297" preserveAspectRatio="none" aria-hidden="true">
    <defs>
      <linearGradient id="frontOrange" x1="0" y1="0" x2="1" y2="0">
        <stop offset="0" stop-color="#ef7c2d"/>
        <stop offset=".6" stop-color="#f0852f"/>
        <stop offset=".78" stop-color="#f39a4a"/>
        <stop offset="1" stop-color="#ef7c2d"/>
      </linearGradient>
    </defs>
    <path d="M0,190 Q300,180 520,78 L520,86 Q300,192 0,202 Z" fill="#424242"/>
    <path d="M0,202 Q300,192 520,86 L520,297 L0,297 Z" fill="url(#frontOrange)"/>
  </svg>

  <div class="brand-name">BROVATEK</div>

  <ul class="contact-list">
    <li>1-800-563-1804 (T)
      <svg viewBox="0 0 12 12"><path d="M2 1.5h2.2l1 2.6-1.3.8a6 6 0 0 0 3.2 3.2l.8-1.3 2.6 1v2.2A1 1 0 0 1 9.5 11 8.5 8.5 0 0 1 1 2.5a1 1 0 0 1 1-1z" fill="#fff"/></svg></li>
    <li>345 555 0192
      <svg viewBox="0 0 12 12"><path d="M2 1.5h2.2l1 2.6-1.3.8a6 6 0 0 0 3.2 3.2l.8-1.3 2.6 1v2.2A1 1 0 0 1 9.5 11 8.5 8.5 0 0 1 1 2.5a1 1 0 0 1 1-1z" fill="#fff"/></svg></li>
    <li>456 555 0137
      <svg viewBox="0 0 12 12"><rect x="3" y="0.8" width="6" height="10.4" rx="1" fill="none" stroke="#fff" stroke-width="1.2"/><circle cx="6" cy="9.4" r=".7" fill="#fff"/></svg></li>
    <li>740-555-0148
      <svg viewBox="0 0 12 12"><rect x="3" y="1" width="6" height="3.5" fill="none" stroke="#fff"/><rect x="1" y="4.5" width="10" height="5" rx="1" fill="#fff"/><rect x="3" y="8" width="6" height="3" fill="#fff" stroke="#ef7c2d" stroke-width=".6"/></svg></li>
    <li>www.brovatek.com
      <svg viewBox="0 0 12 12"><circle cx="6" cy="6" r="5" fill="none" stroke="#fff"/><path d="M1 6h10M6 1c-2.5 3-2.5 7 0 10M6 1c2.5 3 2.5 7 0 10" fill="none" stroke="#fff" stroke-width=".8"/></svg></li>
  </ul>

  <div class="holder">
    <div class="holder-name">Dana Whitfield</div>
    <div>Director</div>
    <div>info@brovatek.com</div>
    <div>218 Kelbrook Lane</div>
    <div>Dunmoor, OH 45790 USA</div>
  </div>
</section>

</body>
</html>
```